TELVA EV

We need a business card design for a new Luxury golf cart Company Telva. We manufacture and sell high end golf carts. We would like to see designs that are high end. I have the logo so really need a nice clean look.

```html
<!DOCTYPE html>
<html lang="en">
<head>
<meta charset="utf-8">
<title>Telva EV — Business Card</title>
<link href="https://fonts.googleapis.com/css2?family=Archivo:wght@800&family=Poppins:wght@400;600&display=swap" rel="stylesheet">
<style>
  :root {
    --backdrop: #5a5a5a;
    --card-white: #ffffff;
    --card-black: #000000;
    --ink: #111111;
    --rule: #c9c9c9;
    --silver-dark: #7a7a7a;
    --silver-light: #f4f4f4;
    --silver-mid: #bdbdbd;
  }
  * { margin: 0; padding: 0; box-sizing: border-box; }
  html, body { width: 1093px; height: 1200px; overflow: hidden; }
  body {
    background: var(--backdrop);
    font-family: "Poppins", sans-serif;
    color: var(--ink);
    position: relative;
  }
  .card {
    position: absolute;
    left: 265px;
    width: 580px;
    height: 357px;
    border-radius: 22px;
    overflow: hidden;
  }
  .card--front { top: 226px; background: var(--card-white); }
  .card--back { top: 621px; background: var(--card-black); }
  .card__band {
    position: absolute;
    left: 0; right: 0; bottom: 0;
    height: 10px;
    background: linear-gradient(90deg, var(--silver-dark), var(--silver-light) 18%, var(--silver-dark) 35%, var(--silver-light) 55%, var(--silver-dark) 72%, var(--silver-light) 90%, var(--silver-mid));
  }
  .brand {
    position: absolute;
    display: flex;
    align-items: center;
    justify-content: center;
    font-family: "Poppins", sans-serif;
    font-weight: 600;
    letter-spacing: 0.08em;
  }
  .card--front .brand {
    left: 28px; top: 157px; width: 231px; height: 60px;
    font-size: 40px; color: var(--ink);
  }
  .card--back .brand {
    left: 113px; top: 132px; width: 354px; height: 92px;
    font-size: 62px; color: var(--silver-mid);
  }
  .divider {
    position: absolute;
    left: 288px; top: 89px;
    width: 1px; height: 175px;
    background: var(--rule);
  }
  .details { position: absolute; left: 313px; top: 91px; }
  .details__name {
    font-family: "Archivo", sans-serif;
    font-weight: 800;
    font-size: 22px;
    line-height: 26px;
    letter-spacing: 0.01em;
  }
  .details__title { font-size: 16px; line-height: 20px; }
  .contact { list-style: none; margin-top: 12px; }
  .contact__item {
    display: flex; align-items: center;
    font-size: 17px; line-height: 22px;
  }
  .contact__icon { width: 17px; height: 17px; margin-right: 10px; flex: none; }
  .address { margin-top: 12px; font-size: 17px; line-height: 21px; font-style: normal; }
</style>
</head>
<body>
  <section class="card card--front">
    <div class="brand">TELVA</div>
    <div class="divider"></div>
    <div class="details">
      <h1 class="details__name">MARCUS HALE</h1>
      <p class="details__title">Managing Director</p>
      <ul class="contact">
        <li class="contact__item">
          <svg class="contact__icon" viewBox="0 0 24 24" aria-hidden="true"><path fill="#111" d="M6.6 10.8a15 15 0 0 0 6.6 6.6l2.2-2.2a1 1 0 0 1 1-.25 11.4 11.4 0 0 0 3.6.57 1 1 0 0 1 1 1V20a1 1 0 0 1-1 1A17 17 0 0 1 3 4a1 1 0 0 1 1-1h3.5a1 1 0 0 1 1 1c0 1.25.2 2.45.57 3.6a1 1 0 0 1-.25 1z"/></svg>
          044-123 456 789
        </li>
        <li class="contact__item">
          <svg class="contact__icon" viewBox="0 0 24 24" aria-hidden="true"><path fill="#111" d="M2 5h20v14H2z"/><path fill="none" stroke="#fff" stroke-width="1.6" d="M2 5l10 8 10-8M2 19l7-7M22 19l-7-7"/></svg>
          info@webname.com
        </li>
        <li class="contact__item">
          <svg class="contact__icon" viewBox="0 0 24 24" aria-hidden="true"><g fill="none" stroke="#111" stroke-width="1.8"><circle cx="12" cy="12" r="10"/><ellipse cx="12" cy="12" rx="4.5" ry="10"/><path d="M2 12h20M4 7h16M4 17h16"/></g></svg>
          www.websitename.com
        </li>
      </ul>
      <address class="address">421, Address line here<br>Country Name, 45452</address>
    </div>
    <div class="card__band"></div>
  </section>

  <section class="card card--back">
    <div class="brand">TELVA</div>
    <div class="card__band"></div>
  </section>
</body>
</html>
```